THE NAME OF THE COMPANY IS: VERDANT HOLLOWS. Services including: Excavation , Custom Property Designs, Sustainable Vegetable Gardens, Beautiful Floriculture. Licensed Contractor with 35 years experience. I am looking for 4 simple Icons: One a tractor, signifying the Excavation work, one a pencil and paper or ruler or something to signify Custom Designs, one a vegetable and one a flower. Similar Icons to the Moss Harbor Logos (attached). The Icons will all be simple but easily identifiable. All of them should look in the same style. I am thinking about a color screen of various olive toned greens. See PMS color chart attached.Probably a white reverse in green tone squares. I'd be interested in different layouts of a business card which will translate to signs and truck door magnets for a full sized truck. It'd also need it to translate to stationary and give away items.

Target Market(s)

The target market is a homeowner with disposable inclome to afford a high end Landscape Artist.

Industry/Entity Type

Business

Contact Information for Business Card

Verdant Hollows
Excavation, Custom Designs, Sustainable Gardens, Floriculture
Howard Pellin
Contractor
Ca. Lic. # C27-591046
PO Box 208716 Carlsbad, Ca 92013
760-382-9174

Colors
acd036
33b7a4

Requirements
Must have
• The company name VERDANT HOLLOWS needs to be prominent with the tag line: Excavation, Custom Property Designs, Sustainable Gardens and Floraculture being centered underneath the name. Be creative with the card color and use different shades of the greens I provided for the icons.

```html
<!DOCTYPE html>
<html lang="en">
<head>
<meta charset="utf-8">
<title>Verdant Hollows – Business Card</title>
<link href="https://fonts.googleapis.com/css2?family=Roboto:wght@400;500;700;900&display=swap" rel="stylesheet">
<style>
  :root {
    --stage: #2b2b2b;
    --paper: #f1f1ef;
    --ink: #1e1e1e;
    --olive-deep: #7f8f3a;
    --olive: #9aab4a;
    --lime: #acd036;
    --sage: #c9d3a4;
    --mist: #dfe5c9;
    --teal-mist: #bcd9cf;
  }
  * { margin: 0; padding: 0; box-sizing: border-box; }
  html, body {
    width: 1200px; height: 796px; overflow: hidden;
    background: var(--stage);
  }
  .stage {
    width: 1200px; height: 796px;
    display: flex; align-items: center; justify-content: center;
  }
  .card {
    position: relative;
    width: 400px; height: 700px;
    background: var(--paper);
    overflow: hidden;
    font-family: "Roboto", Arial, sans-serif;
    color: var(--ink);
  }
  .facet-band {
    position: absolute; top: 0; left: 0;
    width: 400px; height: 150px;
  }
  .facet-foot {
    position: absolute; bottom: 0; left: 0;
    width: 400px; height: 60px;
  }
  .brand {
    position: absolute; top: 180px; left: 0; width: 100%;
    display: flex; flex-direction: column; align-items: center;
  }
  .brand-mark {
    width: 56px; height: 56px;
    background: var(--olive);
    margin-bottom: 18px;
  }
  .brand-name {
    font-weight: 900;
    font-size: 40px;
    letter-spacing: 1px;
    color: var(--olive);
    text-align: center;
    line-height: 1.05;
  }
  .brand-tagline {
    margin-top: 10px;
    font-size: 9px;
    color: var(--olive-deep);
    text-align: center;
    letter-spacing: 0.3px;
  }
  .contact {
    position: absolute; top: 420px; left: 0; width: 100%;
    text-align: center;
  }
  .contact-name {
    font-weight: 700;
    font-size: 24px;
  }
  .contact-title {
    font-size: 15px;
    margin-top: 4px;
  }
  .contact-details {
    margin-top: 26px;
    font-size: 15px;
    line-height: 1.5;
  }
</style>
</head>
<body>
<main class="stage">
  <section class="card">
    <svg class="facet-band" viewBox="0 0 400 150" role="img" aria-label="Faceted low-poly pattern in soft olive and sage greens">
      <defs>
        <linearGradient id="bandTone" x1="1" y1="0" x2="0" y2="1">
          <stop offset="0" stop-color="#9aab4a"/>
          <stop offset="0.45" stop-color="#c9d3a4"/>
          <stop offset="0.75" stop-color="#bcd9cf"/>
          <stop offset="1" stop-color="#dfe5c9"/>
        </linearGradient>
      </defs>
      <polygon points="0,0 400,0 400,150 0,60" fill="url(#bandTone)"/>
    </svg>

    <div class="brand">
      <div class="brand-mark"></div>
      <div class="brand-name">VERDANT<br>HOLLOWS</div>
      <div class="brand-tagline">Excavation, Custom Designs, Sustainable Gardens, Floriculture</div>
    </div>

    <div class="contact">
      <div class="contact-name">Howard Pellin</div>
      <div class="contact-title">Contractor Ca. Lic. # C27-591046</div>
      <div class="contact-details">
        PO Box 208716<br>
        Carlsbad, Ca 92013<br>
        760-382-9174<br>
        www.verdanthollows.com
      </div>
    </div>

    <svg class="facet-foot" viewBox="0 0 400 60" role="img" aria-label="Faint faceted olive pattern along the lower edge">
      <defs>
        <linearGradient id="footTone" x1="0" y1="1" x2="1" y2="0">
          <stop offset="0" stop-color="#c9d3a4"/>
          <stop offset="1" stop-color="#f1f1ef"/>
        </linearGradient>
      </defs>
      <polygon points="0,10 220,60 0,60" fill="url(#footTone)"/>
    </svg>
  </section>
</main>
</body>
</html>
```